Tr construction holdings pty ltd

2 sided card black and red with white
Very professional and elegant

Target Market(s)

Construction and Development

Industry/Entity Type

Construction and development

Contact Information for Business Card

One side black, one side red/or white business logo in top corner, email: morgan@trbuildworks.example

Requirements
Should not have
• Blue

```html
<!DOCTYPE html>
<html lang="en">
<head>
<meta charset="utf-8">
<title>TR Construction Holdings – Business Card</title>
<link rel="stylesheet" href="https://fonts.googleapis.com/css2?family=Lexend:wght@400;600&display=swap">
<style>
  :root {
    --ink: #111111;
    --paper: #ffffff;
    --signal-red: #e83a1f;
    --edge: #d4d4d4;
  }
  html, body {
    margin: 0;
    padding: 0;
    overflow: hidden;
    background: var(--paper);
  }
  .canvas {
    position: relative;
    width: 983px;
    height: 1200px;
    overflow: hidden;
    font-family: "Lexend", "Helvetica Neue", Arial, sans-serif;
  }
  .card-face {
    position: relative;
    width: 983px;
    height: 600px;
    overflow: hidden;
    box-sizing: border-box;
  }
  .card-face--front {
    background: var(--paper);
    color: var(--ink);
    border: 1px solid var(--edge);
  }
  .card-face--back {
    background: var(--signal-red);
    color: var(--paper);
  }
  .brand-name {
    position: absolute;
    top: 70px;
    right: 78px;
    text-align: right;
    font-weight: 600;
    line-height: 1;
    margin: 0;
  }
  .brand-name__initials {
    display: block;
    font-size: 64px;
    letter-spacing: 2px;
  }
  .brand-name__full {
    display: block;
    margin-top: 8px;
    font-size: 17px;
    letter-spacing: 1.4px;
  }
  .frame-accent {
    position: absolute;
    left: 190px;
    top: 336px;
    width: 340px;
    height: 340px;
    box-sizing: border-box;
    border: 5px solid currentColor;
  }
  .contact-email {
    position: absolute;
    right: 29px;
    top: 546px;
    margin: 0;
    font-size: 25px;
    font-weight: 400;
    letter-spacing: 0.3px;
  }
</style>
</head>
<body>
  <main class="canvas">
    <section class="card-face card-face--front">
      <h1 class="brand-name">
        <span class="brand-name__initials">TR</span>
        <span class="brand-name__full">CONSTRUCTION HOLDINGS</span>
      </h1>
      <div class="frame-accent" aria-hidden="true"></div>
      <p class="contact-email">morgan@trbuildworks.example</p>
    </section>
    <section class="card-face card-face--back">
      <h2 class="brand-name">
        <span class="brand-name__initials">TR</span>
        <span class="brand-name__full">CONSTRUCTION HOLDINGS</span>
      </h2>
      <div class="frame-accent" aria-hidden="true"></div>
      <p class="contact-email">morgan@trbuildworks.example</p>
    </section>
  </main>
</body>
</html>
```